fully distributed
Project: fully distributed
fully distributed  - Information Technology
Creative Brief
Use specific fonts
calibri
Simple
Doug Pelliver
CMO
482 Corwin St , Floor 6 New York NY 10019
doug.pelliver@tulvaro.com
logo only
marcste marcste
on 18 and 19 can you fade the grey a litle so it just looks like a faint color
Xpert Xpert
Sure Sir.
we like some of yr designs can u try the design of 17 with the physical layout of card 2
like what you have started will check each one out
thanks we are looking for stationary too
please add fax number 1 800 937 2584

```html
<!DOCTYPE html>
<html lang="en">
<head>
<meta charset="utf-8">
<title>Tulvaro business card</title>
<link rel="stylesheet" href="https://fonts.googleapis.com/css2?family=Carlito:wght@400;700&display=swap">
<style>
  :root {
    --brand-red: #e3192b;
    --brand-red-deep: #c8101f;
    --brand-red-soft: #f06a74;
    --ink: #3a3a3a;
    --ink-soft: #6a6a6a;
    --card: #ffffff;
    --card-shade: #ececec;
    --backdrop: #e4e2de;
  }
  * { margin: 0; padding: 0; box-sizing: border-box; }
  html, body { width: 1200px; height: 946px; overflow: hidden; }
  body {
    background: var(--backdrop);
    font-family: "Carlito", "Calibri", sans-serif;
    color: var(--ink);
    display: flex;
    flex-direction: column;
    align-items: center;
    justify-content: center;
    gap: 40px;
  }
  .card {
    position: relative;
    width: 720px;
    height: 411px;
    background: var(--card);
    overflow: hidden;
    box-shadow: 0 6px 18px rgba(0,0,0,0.18);
  }
  .card-front .front-art { position: absolute; inset: 0; }
  .logo-block {
    position: absolute;
    left: 150px;
    top: 150px;
    display: flex;
    flex-direction: column;
    align-items: flex-start;
  }
  .logo-plate {
    background: var(--card);
    border-radius: 60px;
    padding: 10px 36px 12px 28px;
    display: flex;
    align-items: center;
    gap: 12px;
  }
  .logo-dot { width: 22px; height: 22px; border-radius: 50%; background: var(--brand-red); }
  .logo-name { font-size: 64px; font-weight: 700; color: var(--ink); line-height: 1; }
  .tagline {
    margin: 8px 0 0 60px;
    font-size: 17px;
    font-weight: 700;
    color: var(--card);
  }
  .dot-band {
    position: absolute;
    left: 0; right: 0;
    height: 34px;
    background: linear-gradient(90deg, var(--brand-red) 0%, var(--brand-red-soft) 50%, var(--brand-red) 100%);
  }
  .dot-band.top { top: 0; }
  .dot-band.bottom { bottom: 0; }
  .rule {
    position: absolute;
    height: 1px;
    background: var(--brand-red);
  }
  .rule.upper { left: 40px; right: 40px; top: 58px; }
  .rule.lower { left: 40px; right: 40px; bottom: 58px; }
  .name-tab {
    position: absolute;
    left: 0;
    top: 130px;
    width: 270px;
    height: 96px;
    background: var(--brand-red);
    border-radius: 0 48px 48px 0;
    color: var(--card);
    padding: 18px 0 0 40px;
  }
  .person-name { font-size: 32px; font-weight: 400; line-height: 1.05; }
  .person-role { font-size: 19px; margin-top: 4px; }
  .contact {
    position: absolute;
    right: 46px;
    top: 128px;
    text-align: right;
    font-size: 17px;
    line-height: 1.3;
    color: var(--ink-soft);
  }
  .contact .gap { height: 12px; }
  .contact-line { display: flex; justify-content: flex-end; align-items: center; gap: 8px; }
  .contact-icon { width: 14px; height: 12px; border-radius: 2px; background: var(--brand-red); }
  .contact-icon.blank { background: transparent; }
</style>
</head>
<body>

  <section class="card card-front" aria-label="Card front">
    <svg class="front-art" viewBox="0 0 720 411" width="720" height="411" aria-hidden="true">
      <path d="M0 0 H640 C720 120 700 300 560 411 H0 Z" fill="var(--card-shade)"/>
      <path d="M0 0 H600 C690 120 660 300 520 411 H0 Z" fill="var(--brand-red)"/>
      <path d="M0 0 H420 C300 60 120 60 0 30 Z" fill="var(--brand-red-deep)" opacity="0.35"/>
    </svg>
    <div class="logo-block">
      <div class="logo-plate">
        <span class="logo-dot"></span>
        <span class="logo-name">tulvaro</span>
      </div>
      <p class="tagline">Teams Anywhere, Simply Run</p>
    </div>
  </section>

  <section class="card card-back" aria-label="Card back">
    <div class="dot-band top" role="img" aria-label="Band of red circles of varied sizes"></div>
    <div class="rule upper"></div>
    <div class="name-tab">
      <p class="person-name">Doug Pelliver</p>
      <p class="person-role">CMO</p>
    </div>
    <div class="contact">
      <p>482 Corwin St , Floor 6</p>
      <p>New York NY 10019</p>
      <div class="gap"></div>
      <p class="contact-line">+1 212 555 0148 <span class="contact-icon"></span></p>
      <p class="contact-line">1 800 937 2584 <span class="contact-icon"></span></p>
      <div class="gap"></div>
      <p class="contact-line">doug.pelliver@tulvaro.com <span class="contact-icon blank"></span></p>
    </div>
    <div class="rule lower"></div>
    <div class="dot-band bottom" role="img" aria-label="Band of red circles of varied sizes"></div>
  </section>

</body>
</html>
```